Web Page for marketing online agency

We are an online marketing agency that is acing the direct response model. We engage with our customers throughout different marketing techniques as research copy-writing, advertisements and content writing. We would need a website design that will have four main aspects: The Vision; stating who we are, The Mission; stating what we do, The Team And It's Values, and a Contact Form. For this design we would want a sharp, clean and smart approach, with illustrated elements or suggestive images. You can use the attached copy, the logo, the USP and the motto. Please integrate them as you see fit while keeping in mind the previous needs and copy. This website is going to be our connection with our possible partners, future colleagues and even our clients. You may submit a design for one page or integrate the 4 different aspects on separate web pages.
Target Market(s)
business partners, future employees, age range 25-60
Industry/Entity Type
Direct Marketing
Number of Pages Required
1 page
Requirements
Must have
- Menu / Header
- 4 Parts or 4 Pages including: vision, mission, team, contact
- Logo
- Motto: Direct Brilliance
- USP: We help people help themselves.
- The copy attached
Nice to have
- Representative illustrated images or elements
Should not have
- A boring design, classical design - WordPress like

```html
<!DOCTYPE html>
<html lang="en">
<head>
<meta charset="utf-8">
<title>NovaKin — We help people help themselves</title>
<link href="https://fonts.googleapis.com/css2?family=Questrial&family=Open+Sans:wght@400;600;700&display=swap" rel="stylesheet">
<style>
:root{
  --accent:#3ea8e0;
  --ink:#ffffff;
  --muted:#b9bec4;
  --dark:#2a2a2b;
  --darker:#1f2023;
  --field:#ffffff;
}
*{box-sizing:border-box;margin:0;padding:0}
html,body{width:1200px;height:3879px;overflow:hidden}
body{background:var(--dark);color:var(--ink);font-family:"Open Sans",Arial,sans-serif;position:relative}
.head{font-family:"Questrial",Arial,sans-serif;text-transform:uppercase;text-align:center}
.section{position:absolute;left:0;width:1200px}
.photo{position:absolute;inset:0}

/* hero */
.hero{top:0;height:620px}
.hero .photo{background:linear-gradient(180deg,#3a3d42 0%,#2e3136 55%,#2a2a2b 100%)}
.topbar{position:absolute;top:36px;left:98px;right:20px;height:44px;display:flex;align-items:center}
.logo{font-family:"Questrial",sans-serif;font-size:34px;color:var(--ink);line-height:1}
.nav{display:flex;gap:26px;margin-left:110px;font-family:"Questrial",sans-serif;font-size:14px;font-weight:600}
.nav a{color:var(--ink);text-decoration:none}
.btn-contact{margin-left:auto;background:var(--accent);color:var(--ink);font-family:"Questrial",sans-serif;font-size:13px;padding:14px 30px;border-radius:22px 0 0 22px}
.hero-title{position:absolute;left:238px;top:255px;font-family:"Questrial",sans-serif;font-size:72px;letter-spacing:1px;font-weight:700;line-height:1.15}
.hero-bar{position:absolute;left:414px;top:346px;width:478px;height:8px;background:var(--accent)}
.hero-sub{position:absolute;left:414px;top:370px;font-family:"Questrial",sans-serif;font-size:42px;letter-spacing:1px;line-height:1.15}
.bulb{position:absolute;left:855px;top:238px}
.down{position:absolute;left:908px;top:378px}

/* vision */
.vision{top:620px;height:769px}
.vision h2{position:absolute;top:118px;width:100%;font-size:42px}
.vision h3{position:absolute;top:168px;width:100%;font-size:24px;font-weight:400}
.lead{position:absolute;top:248px;left:130px;width:940px;text-align:center;font-size:19px;line-height:28px}
.body-copy{position:absolute;top:326px;left:110px;width:980px;text-align:center;font-size:13.5px;line-height:22px;color:var(--muted)}
.body-copy b{color:var(--ink)}
.values-title{position:absolute;top:578px;width:100%;font-size:22px}
.value{position:absolute;top:640px;width:140px;text-align:center;font-size:13px;color:var(--muted)}
.value span{display:block;margin:0 auto 10px;width:52px;height:52px;border:2px solid var(--accent);border-radius:50%;color:var(--accent);font-family:"Questrial",sans-serif;font-size:24px;line-height:48px}

/* mission */
.mission{top:1389px;height:512px;display:flex}
.half{position:relative;width:600px;height:512px}
.half.left .photo{background:linear-gradient(135deg,#2b4055,#1f2e3d)}
.half.right .photo{background:linear-gradient(135deg,#2f4153,#24313f)}
.half h2{position:absolute;top:58px;width:100%;font-size:40px}
.half h3{position:absolute;top:106px;width:100%;font-size:24px;font-weight:400}
.half p{position:absolute;top:182px;left:110px;width:390px;text-align:center;font-size:13.5px;line-height:26px}
.half ol{position:absolute;top:182px;left:90px;width:430px;text-align:center;list-style:none;font-size:13.5px;line-height:26px}

/* team */
.team{top:1901px;height:1422px;background:var(--dark)}
.team h2{position:absolute;top:52px;width:100%;font-size:40px}
.team h3{position:absolute;top:98px;width:100%;font-size:24px;font-weight:400}
.team .intro{position:absolute;top:164px;left:120px;width:960px;text-align:center;font-size:18px;line-height:28px}
.traits{position:absolute;top:240px;left:98px;width:620px;list-style:none}
.traits li{font-size:13.5px;color:var(--muted);margin-bottom:26px;line-height:22px}
.traits b{display:block;color:var(--ink);font-weight:600}
.idea-art{position:absolute;left:800px;top:240px;width:271px;height:400px;border-radius:50% 50% 30% 30%;background:radial-gradient(circle at 50% 35%,#3c6f8f 0%,#2f3e4b 60%,#2a2a2b 100%)}
.member{position:absolute;top:770px;width:480px;text-align:center}
.portrait{width:220px;height:220px;margin:0 auto;border-radius:50%;border:6px solid #444;background:linear-gradient(180deg,#8a8f96,#4a4e54)}
.member h4{font-family:"Questrial",sans-serif;font-size:26px;margin-top:32px;line-height:1.2}
.member .role{font-family:"Questrial",sans-serif;font-size:15px;margin-top:2px}
.member p{font-size:12.5px;line-height:20px;color:var(--muted);margin-top:12px}
.member p b{color:var(--ink)}

/* contact */
.contact{top:3323px;height:427px}
.contact .photo{background:linear-gradient(180deg,#2b3a4a,#1d2a37)}
.contact h2{position:absolute;top:40px;width:100%;font-size:40px}
.contact h3{position:absolute;top:88px;width:100%;font-size:22px;font-weight:400}
.field{position:absolute;background:var(--field);color:#777;font-size:11px;padding:10px 10px}
.submit{position:absolute;left:918px;top:308px;width:124px;height:34px;background:var(--accent);color:var(--ink);font-size:12px;font-weight:700;text-align:center;line-height:34px}
.code{position:absolute;right:10px;top:9px;color:#222;font-weight:700}

/* footer */
.footer{top:3750px;height:129px;background:var(--darker);text-align:center}
.up{position:absolute;left:580px;top:-22px}
.copy{position:absolute;top:40px;width:100%;font-size:11px;color:var(--muted)}
.social{position:absolute;top:76px;left:0;width:100%;display:flex;justify-content:center;gap:10px}
.social span{width:26px;height:26px;border-radius:50%;background:#55585d}
</style>
</head>
<body>

<section class="section hero">
  <div class="photo" role="img" aria-label="Photo of a team meeting around a table, darkened"></div>
  <header class="topbar">
    <div class="logo">NovaKin</div>
    <nav class="nav"><a href="#vision">VISION</a><a href="#mission">MISSION</a><a href="#team">TEAM</a></nav>
    <div class="btn-contact">✉ CONTACT US</div>
  </header>
  <h1 class="hero-title">WE HELP PEOPLE</h1>
  <svg class="bulb" width="110" height="110" viewBox="0 0 110 110" fill="none" stroke="#fff" stroke-width="4" stroke-linecap="round">
    <path d="M40 62a22 22 0 1 1 30 0c-4 4-5 8-5 12H45c0-4-1-8-5-12z"/>
    <line x1="45" y1="82" x2="65" y2="82"/><line x1="48" y1="90" x2="62" y2="90"/>
    <line x1="55" y1="4" x2="55" y2="16"/><line x1="20" y1="18" x2="28" y2="26"/><line x1="90" y1="18" x2="82" y2="26"/>
    <line x1="6" y1="48" x2="18" y2="48"/><line x1="92" y1="48" x2="104" y2="48"/>
  </svg>
  <div class="hero-bar"></div>
  <div class="hero-sub">HELP THEMSELVES.</div>
  <svg class="down" width="38" height="38" viewBox="0 0 38 38" fill="none" stroke="#3ea8e0" stroke-width="2.5"><circle cx="19" cy="19" r="17"/><path d="M12 16l7 7 7-7"/></svg>
</section>

<section class="section vision" id="vision">
  <h2 class="head">Our Vision</h2>
  <h3 class="head">Who we are?</h3>
  <p class="lead">We are a direct response company that creates and sells information products and services that millions of people find interesting and important in their lives.</p>
  <p class="body-copy">We are specialized in the self-reliance market and we serve conservative Americans. We are in this business to serve globally and to grow individually. What we serve and inspire are people who need safety, comfort and peace of mind.<br>
  We deliver <b>empowerment</b> through products that create fertile <b>shortcuts</b> to solutions, <b>disentangle</b> reality, <b>simplify</b> choices and ultimately <b>make lives better</b>. We give <b>reassurance</b> and <b>confidence</b> to these people through fresh, unique solutions. We get our <b>inspiration</b> from <b>modern heroes</b> and make their stories available for others. In a way we are <b>democratizing wisdom</b> because we solve serious problems shared by millions of people worldwide. We might not directly save lives, but we try to make a change. We help people help themselves.
  With our thirst for knowledge and drive for constant improvement, we know we'll find a solution to any challenge. And while doing that, we decided to <b>water our inner seeds and harvest the best of our humanity</b>. We invest time and energy in becoming better <b>in the competition with ourselves. We believe that our better selves of tomorrow will nurture better tomorrows for others.</b></p>
  <div class="values-title head">Values</div>
  <div class="value" style="left:155px"><span>1</span>Fairness</div>
  <div class="value" style="left:333px"><span>2</span>Caring</div>
  <div class="value" style="left:512px"><span>3</span>Safety</div>
  <div class="value" style="left:688px"><span>4</span>Freedom</div>
  <div class="value" style="left:864px"><span>5</span>Unconditioned help</div>
</section>

<section class="section mission" id="mission">
  <div class="half left">
    <div class="photo" role="img" aria-label="Photo of a person working at a laptop, blue tinted"></div>
    <h2 class="head">Our Mission</h2>
    <h3 class="head">What is it that we do?</h3>
    <p><b>Lorem Ipsum</b> is simply dummy text of the printing and typesetting industry. <b>Lorem Ipsum</b> has been the industry's standard dummy text ever since the 1500s, when an unknown printer took a galley of type and scrambled it to make a type specimen book. It has survived not only five centuries, but also the leap into electronic typesetting, remaining essentially.</p>
  </div>
  <div class="half right">
    <div class="photo" role="img" aria-label="Photo of hands typing on a keyboard, blue tinted"></div>
    <h2 class="head">We Live and Breathe</h2>
    <h3 class="head">Direct response marketing.</h3>
    <ol>
      <li>i. We are masters of direct response marketing.</li>
      <li>Our expertise is three folded:</li>
      <li>1. We create and aggregate great information products.</li>
      <li>2. We write content that compels people to act.</li>
      <li>3. We do deep research to offer simple quick and easy solutions to people's most serious problems.</li>
      <li>ii. We create content and build solutions to profound challenges for millions of people.</li>
    </ol>
  </div>
</section>

<section class="section team" id="team">
  <h2 class="head">Our Team</h2>
  <h3 class="head">&amp; Values</h3>
  <p class="intro">We're a small team of smart, funny hard-working specialists who are pushing to become the #1 company in self-reliance. High ambition, radical honesty and a result-oriented mindset are encouraged at NovaKin.</p>
  <ul class="traits">
    <li><b>Impact:</b>Leverage, maximum results, 80/20, greatness</li>
    <li><b>Wisdom:</b>Learning mode "on", practice of self-improvement as a lifestyle</li>
    <li><b>Team spirit:</b>Cooperation and complementarity, synergy, yin &amp; yang</li>
    <li><b>Courage:</b>Feel the fear and do it anyway</li>
    <li><b>Innovation mindset:</b>You recombine and reconnect things, so you can solve old problems in new, better ways.</li>
    <li><b>Ownership:</b>"Leaders must own everything in their world. There is no one else to blame."</li>
  </ul>
  <div class="idea-art" role="img" aria-label="Illustration of a light bulb made of colourful marketing icons"></div>

  <div class="member" style="left:99px">
    <div class="portrait" role="img" aria-label="Portrait photo of the CEO"></div>
    <h4>DARIAN HOLT</h4>
    <div class="role">CEO NOVAKIN</div>
    <p>Darian started or was involved in 15 failed businesses before discovering online copywriting. After that, he ended up writing for Brightwell Co and did 10-12 "successful" projects there, at least 3 of which broke the million-dollar mark. He wrote the famous HearthPower sales letter, the infamous CoilInsight and Perrin Motor sales letters.<br>
    In 2012 Darian decided to start his own business, and to sell legit products he and his team could actually be proud of. Six months into the business they had Homestead Freedom, a legendary aquaponics/survival food offer that did over 150,000 initial sales. Ever since, they've been doing successful survival offers, and are one of the few "survival" players constantly coming up with new offers.<br>
    Key personal strengths: copywriting, consulting, positioning, idea generation, mentoring.</p>
  </div>
  <div class="member" style="left:616px">
    <div class="portrait" role="img" aria-label="Portrait photo of the cofounder"></div>
    <h4>MILO VARGA</h4>
    <div class="role">COFOUNDER &amp; AFFILIATE MANAGER NOVAKIN</div>
    <p>Since the company's late 2012 start, Milo grew a network of <b>5000 affiliates</b>, that dominates OfferHub's survival niche - <b>3 out of top 5 products</b> are NovaKin offers, under the Preparedpath brand.<br>
    He currently oversees sales of <b>$10 million / year</b>, management of a <b>160k+</b> email list, marketing, business development and human resources for both the local NovaKin team and the international one.<br>
    Strengths: strong networking skills, sales, risk management, leadership.</p>
  </div>
</section>

<section class="section contact" id="contact">
  <div class="photo" role="img" aria-label="Photo of a city skyline at dusk, darkened"></div>
  <h2 class="head">Contact Us</h2>
  <h3 class="head">Get in touch</h3>
  <div class="field" style="left:160px;top:194px;width:430px;height:150px">Message</div>
  <div class="field" style="left:613px;top:194px;width:429px;height:36px">Name</div>
  <div class="field" style="left:613px;top:251px;width:429px;height:34px">Email</div>
  <div class="field" style="left:613px;top:308px;width:292px;height:34px">Type the code shown<span class="code">HG845</span></div>
  <div class="submit">SUBMIT</div>
</section>

<footer class="section footer">
  <svg class="up" width="40" height="40" viewBox="0 0 40 40"><circle cx="20" cy="20" r="20" fill="#3ea8e0"/><path d="M12 23l8-8 8 8" fill="none" stroke="#fff" stroke-width="3"/></svg>
  <div class="copy">Copyright © 2016 <b>NovaKin</b>. All Rights Reserved</div>
  <div class="social"><span></span><span></span><span></span></div>
</footer>

</body>
</html>
```